Webdesign für Arztpraxis
Zielgruppe
Arztpraxis für Dermatologie am Lindenhof.
Lindenhof ist ein Spital/Krankenhaus hier in Basel, Schweiz.
Kunden sind in jeder Altersstufe für Hauterkrankungen.
Behandlung Chirugisch, konservativ und mit Laser.
Aufgabenstellung
Brandguide und Logo anbei
Farben: #395722 und #ABCF8A
Beispielseite, die gefällt: https://hautpraxis-brunner-kessler.example

```html
<!DOCTYPE html>
<html lang="de">
<head>
<meta charset="utf-8">
<title>Dermatologie am Lindenhof</title>
<link rel="stylesheet" href="https://fonts.googleapis.com/css2?family=Poppins:wght@300;400;500;600&display=swap">
<style>
  :root {
    --green-dark: #395722;
    --green-light: #ABCF8A;
    --green-text: #8fbf6a;
    --sky: #E8F4FC;
    --ink: #111;
    --body: #333;
    --muted: #777;
    --white: #fff;
  }
  * { box-sizing: border-box; margin: 0; padding: 0; }
  html, body { width: 1200px; height: 664px; overflow: hidden; background: var(--white); }
  body { font-family: "Poppins", sans-serif; position: relative; color: var(--body); }

  .hero-band {
    position: absolute; left: 0; top: 0; width: 1200px; height: 50px;
    background: linear-gradient(90deg, #6b5a48 0%, #c9bfb4 18%, #e6ddd4 40%, #7c8a5e 52%, #e2d8ce 65%, #bfb3a6 85%, #5d6a45 100%);
  }

  .quick-nav { position: absolute; top: 26px; left: 167px; display: flex; gap: 12px; z-index: 2; }
  .quick-nav a {
    width: 208px; height: 50px; background: var(--white); border-radius: 22px;
    display: flex; align-items: center; padding: 0 14px 0 16px;
    text-decoration: none; color: var(--green-dark); font-size: 11.5px; font-weight: 500;
    box-shadow: 0 2px 6px rgba(0,0,0,.06);
  }
  .quick-nav .label { flex: 1; }
  .quick-nav .label.centered { text-align: center; }
  .quick-nav svg { flex: none; }
  .quick-nav .icon { margin-right: 8px; }

  .about { position: absolute; top: 50px; left: 0; width: 1200px; height: 340px; background: var(--sky); }
  .portrait {
    position: absolute; left: 167px; top: 46px; width: 217px; height: 262px;
    border-radius: 90px 0 0 0; background: linear-gradient(180deg, #f3f1ee 0%, #ebe7e2 55%, #2a2d3a 56%, #1d2030 100%);
  }
  .about-text { position: absolute; left: 410px; top: 52px; width: 340px; }
  .eyebrow { font-size: 7.5px; color: var(--green-text); }
  .about-text h1 { font-size: 19px; font-weight: 600; color: var(--ink); margin: 1px 0 6px; line-height: 26px; }
  .about-text p { font-size: 9.5px; line-height: 15px; font-weight: 300; color: var(--body); }
  .btn-outline {
    position: absolute; left: 410px; top: 246px; width: 148px; height: 29px;
    border: 1px solid var(--green-light); border-radius: 15px; background: var(--white);
    display: flex; align-items: center; justify-content: center; gap: 34px;
    font-size: 10px; color: var(--green-text); text-decoration: none; padding-left: 20px;
  }
  .consult-photo {
    position: absolute; left: 790px; top: 74px; width: 245px; height: 216px; border-radius: 4px;
    background: linear-gradient(110deg, #d9c7a8 0%, #e8dccb 35%, #f2f3f4 50%, #b9d4bd 75%, #d2c8b6 100%);
  }

  .services { position: absolute; top: 390px; left: 0; width: 1200px; height: 274px; }
  .services-head { text-align: center; margin-top: 28px; }
  .services-head .eyebrow { font-size: 8px; }
  .services-head h2 { font-size: 15.5px; font-weight: 500; color: var(--ink); margin-top: 1px; }
  .service-list { position: absolute; left: 167px; top: 72px; display: flex; gap: 36px; }
  .service { width: 145px; }
  .service .thumb { width: 145px; height: 140px; border-radius: 4px; }
  .service h3 { font-size: 10px; font-weight: 500; color: var(--green-text); margin-top: 10px; line-height: 14px; }
  .service span { font-size: 9.5px; color: var(--muted); font-weight: 300; line-height: 14px; display: block; }
  .t1 { background: linear-gradient(135deg, #e9d3c4, #c99b84); }
  .t2 { background: linear-gradient(135deg, #7f9ccd, #c3d3ea); }
  .t3 { background: linear-gradient(180deg, #5db4ec, #2f7fc4); }
  .t4 { background: linear-gradient(180deg, #a9cff2 0%, #dfeefa 55%, #7ea24d 100%); }
  .t5 { background: linear-gradient(135deg, #f0ddd2, #3d6fc8); }
  .slider-arrow {
    position: absolute; top: 178px; width: 22px; height: 22px; border-radius: 50%;
    background: #e6e6e6; display: flex; align-items: center; justify-content: center;
  }
  .slider-arrow.prev { left: 151px; }
  .slider-arrow.next { left: 1027px; }
  .dots { position: absolute; top: 262px; left: 0; width: 1200px; display: flex; justify-content: center; gap: 4px; }
  .dots i { width: 6px; height: 6px; border-radius: 50%; background: #ddd; }
  .dots i.active { background: #bbb; }
</style>
</head>
<body>
  <div class="hero-band" role="img" aria-label="Fassade des Praxisgebäudes"></div>

  <nav class="quick-nav">
    <a href="#">
      <svg class="icon" width="24" height="24" viewBox="0 0 24 24" fill="none" stroke="#395722" stroke-width="1.1"><rect x="2" y="4" width="18" height="17" rx="3"/><path d="M2 9h18M7 2v4M15 2v4"/><circle cx="18" cy="18" r="4" fill="#fff"/><path d="M16.3 18l1.2 1.2 2.2-2.2"/></svg>
      <span class="label">Termine Buchen</span>
      <svg width="16" height="12" viewBox="0 0 16 12" fill="none" stroke="#395722" stroke-width="1.2"><path d="M1 6h13M9 1l5 5-5 5"/></svg>
    </a>
    <a href="#">
      <svg class="icon" width="22" height="22" viewBox="0 0 24 24" fill="none" stroke="#395722" stroke-width="1.2"><path d="M5 3l3 0 2 5-2 1.5a11 11 0 0 0 6.5 6.5L16 14l5 2v3a2 2 0 0 1-2 2A17 17 0 0 1 3 5a2 2 0 0 1 2-2z"/><path d="M15 3a6 6 0 0 1 6 6M15 6.5a2.5 2.5 0 0 1 2.5 2.5"/></svg>
      <span class="label">Arzt auf Abruf</span>
      <svg width="16" height="12" viewBox="0 0 16 12" fill="none" stroke="#395722" stroke-width="1.2"><path d="M1 6h13M9 1l5 5-5 5"/></svg>
    </a>
    <a href="#">
      <span class="label centered">Anfahrt</span>
      <svg width="16" height="12" viewBox="0 0 16 12" fill="none" stroke="#395722" stroke-width="1.2"><path d="M1 6h13M9 1l5 5-5 5"/></svg>
    </a>
    <a href="#">
      <span class="label centered">Öffnungszeiten</span>
      <svg width="16" height="12" viewBox="0 0 16 12" fill="none" stroke="#395722" stroke-width="1.2"><path d="M1 6h13M9 1l5 5-5 5"/></svg>
    </a>
  </nav>

  <section class="about">
    <div class="portrait" role="img" aria-label="Porträt des Praxisinhabers"></div>
    <div class="about-text">
      <div class="eyebrow">Über Uns</div>
      <h1>Dermatologie am Lindenhof</h1>
      <p>Dermatologie am Lindenhof ist eine moderne Praxis für allgemeine und ästhetische Dermatologie. Wir behandeln und beraten Sie bei allen Hauterkrankungen, Hautkrebs und Allergien.<br>
      Wenn es darum geht, sich einfach wieder gut und schön zu fühlen in Ihrer Haut profitieren Sie von unserer Expertise in Lasermedizin und Soft-Ästhetik.<br>
      Wir sind jederzeit gerne für Sie da!&nbsp; Kontaktieren Sie uns, um Ihre individuellen Anliegen und Fragen zu besprechen.</p>
    </div>
    <a class="btn-outline" href="#">Über Uns
      <svg width="10" height="8" viewBox="0 0 10 8" fill="none" stroke="#8fbf6a" stroke-width="1"><path d="M0 4h9M6 1l3 3-3 3"/></svg>
    </a>
    <div class="consult-photo" role="img" aria-label="Arzt untersucht die Hand einer Patientin"></div>
  </section>

  <section class="services">
    <div class="services-head">
      <div class="eyebrow">Dermatologie</div>
      <h2>Leistungsspektrum</h2>
    </div>
    <div class="service-list">
      <div class="service"><div class="thumb t1" role="img" aria-label="Hautuntersuchung mit Dermatoskop"></div><h3>Allgemeine Dermatologie</h3><span>mehr erfahren</span></div>
      <div class="service"><div class="thumb t2" role="img" aria-label="Chirurgische Instrumente im Operationssaal"></div><h3>Dermatochirurgie</h3><span>mehr erfahren</span></div>
      <div class="service"><div class="thumb t3" role="img" aria-label="Lichttherapie-Kabine"></div><h3>Lichttherapie</h3><span>mehr erfahren</span></div>
      <div class="service"><div class="thumb t4" role="img" aria-label="Pusteblumen auf einer Wiese"></div><h3>Allergologie</h3><span>mehr erfahren</span></div>
      <div class="service"><div class="thumb t5" role="img" aria-label="Laserbehandlung auf der Haut"></div><h3>Lasermedizin</h3><span>mehr erfahren</span></div>
    </div>
    <div class="slider-arrow prev"><svg width="8" height="10" viewBox="0 0 8 10" fill="none" stroke="#fff" stroke-width="1.2"><path d="M6 1L2 5l4 4"/></svg></div>
    <div class="slider-arrow next"><svg width="8" height="10" viewBox="0 0 8 10" fill="none" stroke="#fff" stroke-width="1.2"><path d="M2 1l4 4-4 4"/></svg></div>
    <div class="dots"><i class="active"></i><i></i><i></i><i></i></div>
  </section>
</body>
</html>
```